A private security company called "Tavrin Security Services Ltd"

Hello everybody,

We need a web page for a company based in NZ. It is mainly an informative website so it would be wonderful if the designer puts their absolute best into making it a website that I would really appreciate. The website needs to show professionalism and also needs to make our web surfers find the information they need in a click. the company's colour is black and silver, and if those two colours could be integrated into the website it would be absolutely lovely. Please do contact me for any information.

Sincerely,
Dorian Velasko

Industry/Entity Type

Security

```html
<!DOCTYPE html>
<html lang="en">
<head>
<meta charset="utf-8">
<title>Tavrin Security Services Ltd</title>
<link href="https://fonts.googleapis.com/css2?family=Open+Sans:wght@300;400;600;700&display=swap" rel="stylesheet">
<style>
:root{
  --ink:#1c1c1c;
  --charcoal:#262626;
  --graphite:#3a3a3a;
  --silver:#c9c9c9;
  --silver-light:#e8e8e8;
  --mist:#f4f4f4;
  --muted:#8a8a8a;
  --body:#555;
  --white:#fff;
  --accent:#e8562a;
  --heart:#d0202a;
}
*{box-sizing:border-box;margin:0;padding:0}
html,body{width:685px;height:1200px;overflow:hidden}
body{font-family:"Open Sans",Arial,sans-serif;color:var(--ink);background:var(--white);position:relative}

/* header */
.site-header{position:absolute;top:0;left:0;width:685px;height:50px;background:var(--silver-light);border-bottom:1px solid #d4d4d4}
.brand{position:absolute;left:16px;top:14px;display:flex;align-items:center;gap:5px}
.brand-mark{width:10px;height:10px;background:var(--ink);border-radius:50%}
.brand-name{font-size:9px;font-weight:700;color:var(--ink);letter-spacing:.5px;line-height:1.1;text-transform:uppercase}
.main-nav{position:absolute;left:177px;top:18px;display:flex;gap:0}
.main-nav a{display:block;font-size:6.4px;color:#444;text-decoration:none;padding:3px 7px;line-height:8px;text-transform:uppercase}
.main-nav a.is-active{background:#6e6e6e;color:var(--white);border-radius:1px}
.search{position:absolute;left:460px;top:16px;width:115px;height:18px;background:var(--white);border-radius:9px;border:1px solid #ddd}
.search span{position:absolute;left:11px;top:4px;font-size:6px;color:#aaa}
.search svg{position:absolute;right:10px;top:4px}
.phone{position:absolute;left:597px;top:20px;display:flex;align-items:center;gap:4px;font-size:6.4px;color:#333}

/* hero */
.hero{position:absolute;top:50px;left:0;width:685px;height:283px;overflow:hidden}
.hero-media{position:absolute;inset:0;background:linear-gradient(110deg,#1d2630 0%,#3a4750 45%,#5f6a5e 75%,#4a5548 100%)}
.hero-shade{position:absolute;inset:0;background:rgba(0,0,0,.28)}
.hero-title{position:absolute;top:48px;width:100%;text-align:center;color:var(--white);font-size:37px;font-weight:700;letter-spacing:2.6px;line-height:45px}
.hero-btn{position:absolute;left:278px;top:158px;width:128px;height:30px;border:1px solid rgba(255,255,255,.8);border-radius:2px;color:var(--white);font-size:9.5px;text-align:center;line-height:28px;text-transform:uppercase;letter-spacing:.3px;background:rgba(0,0,0,.25)}

/* shared */
.divider{display:flex;justify-content:center;margin:0 auto}
.divider i{display:block;width:21px;height:2px;background:var(--graphite)}
.divider i+i{background:var(--silver)}
.section-title{text-align:center}

/* about */
.about{position:absolute;top:333px;left:0;width:685px;height:143px;background:var(--white)}
.about .section-title{margin-top:38px;font-size:16px;font-weight:700;letter-spacing:.6px;color:var(--ink)}
.about .section-title span{font-weight:400;color:var(--muted)}
.about p{width:370px;margin:10px auto 0;font-size:5.9px;line-height:10px;color:#666;text-align:center;text-transform:uppercase;letter-spacing:.2px}
.about .divider{margin-top:8px}

/* services */
.services{position:absolute;top:476px;left:0;width:685px;height:220px;background:var(--charcoal)}
.services .section-title{margin-top:19px;font-size:14.5px;font-weight:400;color:var(--silver);letter-spacing:1px}
.services .divider{margin-top:11px}
.services .divider i{background:#151515}
.services .divider i+i{background:var(--silver)}
.service-row{position:absolute;top:70px;left:16px;width:653px;display:flex}
.service{width:163.25px;text-align:center;color:var(--white)}
.service svg{display:block;margin:0 auto;height:50px}
.service h3{margin-top:7px;font-size:8px;font-weight:600;letter-spacing:.4px}
.service p{margin-top:4px;font-size:5.8px;line-height:9px;color:#ddd;padding:0 2px}
.btn-more{display:inline-block;margin-top:7px;width:61px;height:20px;line-height:20px;background:var(--silver);color:var(--ink);font-size:6.2px;font-weight:700;border-radius:2px;box-shadow:0 1px 0 #000}

/* what we do */
.what{position:absolute;top:696px;left:0;width:685px;height:227px;background:var(--silver-light)}
.what .section-title{margin-top:24px;font-size:14px;font-weight:400;color:var(--ink);letter-spacing:1px}
.what .divider{margin-top:14px}
.task-row{position:absolute;top:85px;left:0;width:685px}
.task{position:absolute;width:120px;text-align:center}
.task-media{display:block;width:92px;height:58px;margin:0 auto;border-radius:1px}
.task h3{margin-top:9px;font-size:11px;font-weight:600;color:var(--ink);letter-spacing:.4px}
.task p{margin-top:2px;font-size:6px;line-height:9.5px;color:var(--muted)}

/* customers */
.customers{position:absolute;top:923px;left:0;width:685px;height:243px;background:var(--white)}
.customers .section-title{margin-top:20px;font-size:15px;font-weight:700;color:var(--ink);letter-spacing:.6px;display:flex;justify-content:center;align-items:center;gap:6px}
.customers .section-title span{font-weight:400;color:var(--muted)}
.customers .divider{margin-top:11px}
.quote-card{position:absolute;top:98px;width:238px;height:109px;background:var(--ink);border-radius:2px;color:var(--white)}
.avatar{position:absolute;left:12px;top:-19px;width:68px;height:68px;border-radius:50%;border:2px solid var(--white)}
.quote-name{position:absolute;left:0;width:92px;top:56px;text-align:center;font-size:8px;font-weight:400;letter-spacing:.3px}
.quote-open{position:absolute;left:90px;top:14px}
.quote-text{position:absolute;left:81px;top:40px;width:151px;font-size:6.1px;line-height:10px;color:#ddd}
.quote-close{position:absolute;right:20px;top:87px}
.carousel-arrow{position:absolute;top:138px}

/* footer */
.site-footer{position:absolute;top:1166px;left:0;width:685px;height:34px;background:var(--graphite)}
.copyright{position:absolute;left:52px;top:13px;font-size:6.3px;color:#ddd}
.copyright span{color:var(--accent)}
.socials{position:absolute;left:534px;top:7px;display:flex;gap:9px}
.socials i{display:block;width:19px;height:19px;border:1.4px solid var(--white);border-radius:50%}
.to-top{position:absolute;left:329px;top:-14px;width:27px;height:27px;border-radius:50%;background:var(--accent);display:flex;align-items:center;justify-content:center}
</style>
</head>
<body>

<header class="site-header">
  <div class="brand">
    <span class="brand-mark"></span>
    <span class="brand-name">Tavrin</span>
  </div>
  <nav class="main-nav">
    <a class="is-active">Home</a><a>About</a><a>Services</a><a>Compare</a><a>Blog</a><a>Contact</a>
  </nav>
  <div class="search"><span>Search</span>
    <svg width="9" height="9" viewBox="0 0 10 10"><circle cx="4" cy="4" r="3" fill="none" stroke="#888" stroke-width="1"/><line x1="6.2" y1="6.2" x2="9" y2="9" stroke="#888" stroke-width="1.1"/></svg>
  </div>
  <div class="phone">
    <svg width="9" height="9" viewBox="0 0 10 10"><circle cx="5" cy="5" r="4.3" fill="none" stroke="#c62828" stroke-width=".9"/><path d="M3.4 2.8c.3-.3.6-.2.8.1l.4.7c.1.3 0 .5-.2.6l-.2.2c.2.6.6 1 1.2 1.3l.2-.2c.2-.2.4-.2.6-.1l.7.4c.3.2.3.5.1.8-.4.5-.9.6-1.5.3-1.1-.6-1.9-1.4-2.4-2.5-.2-.6 0-1.1.3-1.6z" fill="#c62828"/></svg>
    <span>+1 -555-310-4472</span>
  </div>
</header>

<section class="hero">
  <div class="hero-media" role="img" aria-label="Security operator on the phone in front of surveillance monitors showing an industrial site"></div>
  <div class="hero-shade"></div>
  <h1 class="hero-title">WE ARE HERE TO<br>PROTECT YOUR WORLD</h1>
  <div class="hero-btn">Learn More</div>
</section>

<section class="about">
  <h2 class="section-title"><span>What is</span> Tavrin Security Services</h2>
  <p>Lorem Ipsum is simply dummy text of the printing and typesetting industry. Lorem Ipsum has been the industry's standard dummy text ever since the 1500s, when an unknown printer took a galley of type and scrambled it to make a type specimen book.</p>
  <div class="divider"><i></i><i></i></div>
</section>

<section class="services">
  <h2 class="section-title">OUR SERVICES</h2>
  <div class="divider"><i></i><i></i></div>
  <div class="service-row">
    <div class="service">
      <svg viewBox="0 0 40 46" width="40"><path d="M20 1 38 8v14c0 11-8 19-18 23C10 41 2 33 2 22V8z" fill="#fff"/><path d="M20 13 9 23h3v9h5v-6h6v6h5v-9h3z" fill="#262626"/></svg>
      <h3>HOME SECURITY</h3>
      <p>Lorem Ipsum is simply dummy text of the printing and typesetting industry. Lorem Ipsum has been the industry's standard dummy text ever since the.</p>
      <span class="btn-more">KNOW MORE</span>
    </div>
    <div class="service">
      <svg viewBox="0 0 48 48" width="48"><circle cx="20" cy="11" r="8" fill="#fff"/><path d="M6 44c0-12 6-19 14-19s14 7 14 19z" fill="#fff"/><path d="M34 24l9 3v7c0 6-4 9-9 11-5-2-9-5-9-11v-7z" fill="#262626" stroke="#fff" stroke-width="2"/><path d="M34 28v13c3-1.5 5.5-3.5 5.5-7v-4.5z" fill="#fff"/></svg>
      <h3>BUSINESS SECURITY</h3>
      <p>Lorem Ipsum is simply dummy text of the printing and typesetting industry. Lorem Ipsum has been the industry's standard dummy text ever since the.</p>
      <span class="btn-more">KNOW MORE</span>
    </div>
    <div class="service">
      <svg viewBox="0 0 48 50" width="46"><path d="M6 10h22l6-4h6v14h-6l-6-4H14z" fill="#fff"/><rect x="38" y="2" width="8" height="16" fill="#fff"/><circle cx="20" cy="24" r="4.5" fill="#fff"/><path d="M13 48V36c0-4 3-7 7-7s7 3 7 7v12h-4V40h-6v8z" fill="#fff"/></svg>
      <h3>SECURITY FOR KIDS</h3>
      <p>Lorem Ipsum is simply dummy text of the printing and typesetting industry. Lorem Ipsum has been the industry's standard dummy text ever since the.</p>
      <span class="btn-more">KNOW MORE</span>
    </div>
    <div class="service">
      <svg viewBox="0 0 48 48" width="48"><circle cx="29" cy="19" r="15" fill="none" stroke="#fff" stroke-width="3"/><text x="29" y="25" text-anchor="middle" font-family="Open Sans,Arial,sans-serif" font-size="15" font-weight="700" fill="#fff">24</text><path d="M4 12c3-4 6-4 8-1l4 6c1 2 0 4-2 5l-2 1c2 5 6 9 11 12l1-2c1-2 3-3 5-2l6 4c3 2 3 5-1 8-5 4-10 3-16-1C12 37 7 31 4 25c-2-5-2-9 0-13z" fill="#fff" stroke="#262626" stroke-width="1.5"/></svg>
      <h3>24/7 DEDICATED SUPPORT</h3>
      <p>Lorem Ipsum is simply dummy text of the printing and typesetting industry. Lorem Ipsum has been the industry's standard dummy text ever since the.</p>
      <span class="btn-more">KNOW MORE</span>
    </div>
  </div>
</section>

<section class="what">
  <h2 class="section-title">WHAT WE DO</h2>
  <div class="divider"><i></i><i></i></div>
  <div class="task-row">
    <div class="task" style="left:78px">
      <span class="task-media" role="img" aria-label="Armed security officer in tactical gear" style="background:linear-gradient(90deg,#3a3f44,#c9c7c2)"></span>
      <h3>FIND</h3>
      <p>Lorem Ipsum is simply dummy text of the printing and typesetting industry.</p>
    </div>
    <div class="task" style="left:214px">
      <span class="task-media" role="img" aria-label="Security guard speaking into a radio beside a patrol car" style="background:linear-gradient(135deg,#b8aa8a,#2d3f6a 60%,#8a8f9a)"></span>
      <h3>FIX</h3>
      <p>Lorem Ipsum is simply dummy text of the printing and typesetting industry.</p>
    </div>
    <div class="task" style="left:353px">
      <span class="task-media" role="img" aria-label="Couple holding a phone with a security alert app" style="background:linear-gradient(135deg,#a8452e,#3c3c3c 55%,#c8c2b8)"></span>
      <h3>PREVENT</h3>
      <p>Lorem Ipsum is simply dummy text of the printing and typesetting industry.</p>
    </div>
    <div class="task" style="left:486px">
      <span class="task-media" role="img" aria-label="Operators working at monitoring computers in an office" style="background:linear-gradient(90deg,#e6e6e6,#8c8c8c 60%,#d8d8d8)"></span>
      <h3>ACCELERATE</h3>
      <p>Lorem Ipsum is simply dummy text of the printing and typesetting industry.</p>
    </div>
  </div>
</section>

<section class="customers">
  <h2 class="section-title"><span>We</span>
    <svg width="22" height="19" viewBox="0 0 22 19"><path d="M11 19 2 10C-1 7 0 2 4 1c3-1 5 1 7 3 2-2 4-4 7-3 4 1 5 6 2 9z" fill="var(--heart)"/></svg>
    Our Customers</h2>
  <div class="divider"><i></i><i></i></div>

  <svg class="carousel-arrow" style="left:62px" width="16" height="30" viewBox="0 0 16 30"><path d="M15 1 1 15l14 14" fill="none" stroke="#bbb" stroke-width="1.2"/></svg>
  <svg class="carousel-arrow" style="left:607px" width="16" height="30" viewBox="0 0 16 30"><path d="M1 1l14 14L1 29" fill="none" stroke="#bbb" stroke-width="1.2"/></svg>

  <article class="quote-card" style="left:92px">
    <span class="avatar" role="img" aria-label="Portrait of a customer in a suit" style="background:linear-gradient(160deg,#2b3440,#3d5f9a)"></span>
    <div class="quote-name">MILES HARCOURT</div>
    <svg class="quote-open" width="26" height="18" viewBox="0 0 26 18"><path d="M0 18V10C0 4 3 1 9 0v4C6 5 5 7 5 9h5v9zM14 18V10c0-6 3-9 9-10v4c-3 1-4 3-4 5h5v9z" fill="#fff"/></svg>
    <p class="quote-text">Lorem Ipsum is simply dummy text of the printing and typesetting industry. Lorem Ipsum has been the industry's standard dummy text ever since the 1500s, when an unknown printer.</p>
    <svg class="quote-close" width="11" height="8" viewBox="0 0 26 18"><path d="M26 0v8c0 6-3 9-9 10v-4c3-1 4-3 4-5h-5V0zM12 0v8c0 6-3 9-9 10v-4c3-1 4-3 4-5H2V0z" fill="#fff"/></svg>
  </article>

  <article class="quote-card" style="left:355px">
    <span class="avatar" role="img" aria-label="Portrait of a smiling customer" style="background:linear-gradient(160deg,#6a8fb0,#c8a27a 60%,#2a2a2a)"></span>
    <div class="quote-name">LENA VOSS</div>
    <svg class="quote-open" width="26" height="18" viewBox="0 0 26 18"><path d="M0 18V10C0 4 3 1 9 0v4C6 5 5 7 5 9h5v9zM14 18V10c0-6 3-9 9-10v4c-3 1-4 3-4 5h5v9z" fill="#fff"/></svg>
    <p class="quote-text">Lorem Ipsum is simply dummy text of the printing and typesetting industry. Lorem Ipsum has been the industry's standard dummy text ever since the 1500s, when an unknown printer.</p>
    <svg class="quote-close" width="11" height="8" viewBox="0 0 26 18"><path d="M26 0v8c0 6-3 9-9 10v-4c3-1 4-3 4-5h-5V0zM12 0v8c0 6-3 9-9 10v-4c3-1 4-3 4-5H2V0z" fill="#fff"/></svg>
  </article>
</section>

<footer class="site-footer">
  <div class="to-top"><svg width="11" height="7" viewBox="0 0 11 7"><path d="M1 6 5.5 1.5 10 6" fill="none" stroke="#fff" stroke-width="2"/></svg></div>
  <p class="copyright">Copyright © 2014 - <span>Tavrin Security Services Ltd.</span> All rights reserved.</p>
  <div class="socials"><i></i><i></i><i></i><i></i></div>
</footer>

</body>
</html>
```